1 Page Website Design For Diabetic Discount RX Card

~~I NEED A WEBSITE LANDING PAGE DESIGNED~~:

TITLE: GET UP TO 75% Off ALL YOUR DIABETIC SUPPLIES GUARANTEED
SUBITITLE: Never Pay Full Price For Your Diabetic Supplies Again!

~~FORM~~:
Choose Your Current Brand Of Diabetic Supplies That You Currently Use To See If They Are Covered Under Our Free Diabetic RX Assistance Program:

~~DROP DOWN MENU~~
Acarbose Up To 75% Off!

Zernovab Tel Up To 75% Off!

Zernovab Tel Xr Up To 54% Off!

Wempu Up To 75% Off!

Orvantel Up To 75% Off!

Quilmor Up To 75% Off!

Tesfunn Up To 75% Off!

Wombeth Up To 75% Off!

Elkrostiv Up To 54% Off!

Irmoskuve Up To 54% Off!

Ulpremo Up To 54% Off!

Fashkelin Up To 75% Off!

Kolvrin Up To 75% Off!

Chlorpropamide Up To 75% Off!

Colesevelam Up To 75% Off!

Pembrath Up To 54% Off!

Qwemt Up To 75% Off!

Desmopressin 52% Off

Sornefil 74% Off

Ferlutham Up To 54% Off!
Mirsolk Up To 75% Off!

Kelmuro Up To 75% Off!

Yibrosel Up To 75% Off!

Glimepiride 66% Off

Glipizide Up To 75% Off!

Glipizide Er Up To 75% Off!

Ventrosimel Up To 75% Off!

Ventrosimel Xr Up To 75% Off!

Brastumol Up To 75% Off!

Brastumol Xl Up To 75% Off!

Pelkirona Up To 75% Off!

Sovrinka Up To 75% Off!

Glyburide Up To 75% Off!

Glyburide Micronized Up To 75% Off!
Twerdo Up To 75% Off!

Omrick Up To 75% Off!

Hestrolu Up To 75% Off!

Pirvetan 50 50 Up To 75% Off!

Pirvetan Up To 75% Off!

Vostrek N Up To 75% Off!

Vostrek R Up To 75% Off!

Insulin Detemir Up To 75% Off!

Insulin Glulisine Up To 75% Off!

Selbrudar Up To 75% Off!

Thebrisu Up To 75% Off!

Kwelbor Up To 75% Off!

Kwelbor Xr Up To 75% Off!

Mostrelo Up To 75% Off!

Pelvouste Up To 75% Off!

Wurmbostel Up To 75% Off!

Trevlu Up To 75% Off!

Hustravel Xr Up To 75% Off!

Privok Up To 75% Off!

Dosharp Up To 75% Off!

Ostrubel Up To 54% Off!

Metformin 73% Off

Talverush Up To 54% Off!

Miglitol Up To 75% Off!

Skevrant Up To 33% Off!

Nateglinide Up To 75% Off!

Wolbrey Up To 75% Off!

Piltrago Up To 75% Off!

Kestrub N Up To 75% Off!

Kestrub R Up To 75% Off!

Harpenu Up To 75% Off!

Blemkarsu Up To 33% Off!

Skirvet Up To 75% Off!

Plembuth Up To 54% Off!

Vurlk Up To 75% Off!

Pioglitazone Up To 75% Off!

Pramlintide Up To 75% Off!

Welhostro Up To 54% Off!

Kuvelst Up To 75% Off!

Dimbrul 20% Off

Repaglinide Up To 75% Off!

Sklavon Up To 75% Off!

Rosiglitazone Up To 75% Off!

Sitagliptin Up To 75% Off!

Humbrev Up To 75% Off!

Fortkavul Up To 75% Off!

Pelbruko Up To 75% Off!

Wiskorb Up To 75% Off!

Tolazamide Up To 75% Off!

Tolbutamide Up To 75% Off!

Breshmuv Up To 54% Off!

Skamvi Up To 75% Off!

Huvelpsor Up To 75% Off!

Komplev Up To 75% Off!

Skyvelmon Up To 15% Off!

Bospenarve Up To 75% Off!

Fresvomel Up To 33% Off!

Drumpal Up To 75% Off!

Spirnak Up To 75% Off!

Premvol Xr Up To 75% Off!

~~~~After they choose one I want this message to pop up~~~~:

YES! ~~NAME OF DRUG~~ IS COVERED UNDER OUR FREE DIABETIC RX PROGRAM!
3 EASY WAYS TO RECEIVE YOUR FREE DIABETIC RX ASSISTANCE VOUCHER:

1. Simply Click Below To Download Your Voucher Right Now!

~~DOWNLOAD VOUCHER NOW~~
2. Enter Your Cell Phone Number And We Will Send The Voucher To You By Text Message Instantly:

3. Enter Your Email And We Will Send The Voucher To Your Email Instantly:

Target Market(s)

People with Diabetes

Number of Pages Required

1 page

Colors

Designer to choose colors to be used in the design.

Requirements
Must have
• must be professional looking and build trust and credibility
Nice to have
• Photos of diabetics...real people
Should not have
• red

```html
<!DOCTYPE html>
<html lang="en">
<head>
<meta charset="utf-8">
<title>Sucrana – Diabetic Supplies Discount</title>
<link href="https://fonts.googleapis.com/css2?family=Oswald:wght@400;500&family=Open+Sans:wght@400;600;700&display=swap" rel="stylesheet">
<style>
  :root {
    --teal: #27a4b3;
    --teal-dark: #1f8f9c;
    --button-grey: #5a9aa3;
    --ink: #1c1c1c;
    --white: #ffffff;
    --muted: #7a7a7a;
    --line: #d6e6e9;
  }
  * { box-sizing: border-box; margin: 0; padding: 0; }
  html, body { width: 718px; height: 1200px; overflow: hidden; background: var(--white); }
  body { position: relative; font-family: "Open Sans", Arial, sans-serif; color: var(--ink); }

  .hero { position: absolute; left: 0; top: 0; width: 718px; height: 452px;
    background: linear-gradient(180deg, #5d5555 0%, #7a6a6a 40%, #6b5b5e 70%, #5b5052 100%); }
  .hero-photo { position: absolute; inset: 0;
    background: radial-gradient(ellipse 260px 300px at 360px 170px, rgba(176,140,130,.55), transparent 70%),
                radial-gradient(ellipse 200px 180px at 640px 260px, rgba(90,130,70,.35), transparent 70%); }
  .brand { position: absolute; left: 30px; top: 16px; font-family: "Open Sans", sans-serif; font-weight: 600;
    font-size: 19px; color: var(--teal); letter-spacing: -.3px; }
  .nav { position: absolute; top: 23px; right: 36px; display: flex; gap: 22px; }
  .nav a { font-family: "Oswald", sans-serif; font-size: 8px; color: var(--white); text-decoration: none; }

  .hero-title { position: absolute; top: 152px; left: 0; width: 718px; text-align: center;
    font-family: "Oswald", sans-serif; font-weight: 400; font-size: 24px; line-height: 29px;
    color: var(--white); letter-spacing: -.8px; transform: scaleX(.85); }
  .hero-title u { text-decoration-thickness: 1px; text-underline-offset: 3px; }
  .hero-rule { position: absolute; top: 229px; left: 336px; width: 33px; height: 2px; background: var(--teal); }
  .hero-sub { position: absolute; top: 249px; left: 0; width: 718px; text-align: center;
    font-family: "Oswald", sans-serif; font-size: 10px; color: var(--white); letter-spacing: -.3px; }

  .brand-form { position: absolute; left: 177px; top: 318px; width: 356px; height: 260px;
    background: var(--teal); border-radius: 3px; }
  .form-intro { position: absolute; top: 37px; left: 0; width: 100%; text-align: center;
    font-size: 7px; font-weight: 600; line-height: 9.3px; color: var(--white); letter-spacing: -.2px; }
  .brand-select { position: absolute; left: 95px; top: 79px; width: 181px; background: var(--white);
    border: 1px solid var(--line); }
  .select-head { height: 24px; background: #f4f4f4; display: flex; align-items: center;
    padding-left: 8px; font-size: 7px; color: var(--muted); position: relative; }
  .select-caret { position: absolute; right: 0; top: 0; width: 24px; height: 24px; background: var(--button-grey); }
  .option { height: 25px; border-top: 1px solid #e6eef0; display: flex; align-items: center;
    padding-left: 8px; font-size: 7px; color: var(--muted); position: relative; }
  .option b { font-weight: 400; color: var(--ink); margin-left: 3px; }
  .option.is-selected { color: var(--teal); }
  .radio { position: absolute; right: 11px; top: 8px; width: 9px; height: 9px; border-radius: 50%;
    background: #e3e3e3; }
  .option.is-selected .radio { background: #3b93a3; }
  .scrollbar { position: absolute; right: 2px; top: 28px; width: 1px; height: 14px; background: #777; }
  .choose-btn { position: absolute; left: 132px; top: 196px; width: 103px; height: 24px;
    background: var(--button-grey); color: var(--white); font-size: 7.5px; display: flex;
    align-items: center; justify-content: center; letter-spacing: .2px; }

  .healthy-title { position: absolute; left: 64px; top: 672px; font-family: "Oswald", sans-serif;
    font-weight: 400; font-size: 31px; line-height: 34px; color: var(--ink); transform: scaleX(.9);
    transform-origin: left; }
  .healthy-image { position: absolute; left: 398px; top: 612px; width: 320px; height: 232px;
    background: radial-gradient(ellipse 150px 110px at 150px 130px, #e8b24a 0%, #c9a56a 35%, #e6ded0 70%, rgba(255,255,255,0) 100%); }

  .tips { position: absolute; left: 0; top: 876px; width: 718px; height: 270px;
    background: linear-gradient(90deg, #4a4340 0%, #7d7a72 45%, #a8a39c 75%, #8b8882 100%); }
  .tips-title { position: absolute; top: 104px; left: 0; width: 718px; text-align: center;
    font-family: "Oswald", sans-serif; font-size: 31px; color: var(--white); transform: scaleX(.88); }
  .tips-btn { position: absolute; left: 300px; top: 159px; width: 98px; height: 33px; background: var(--teal);
    color: var(--white); font-family: "Oswald", sans-serif; font-size: 10px; display: flex;
    align-items: center; justify-content: center; }

  .footer { position: absolute; left: 0; top: 1146px; width: 718px; height: 54px; background: var(--teal);
    color: var(--white); font-size: 10px; }
  .footer p { position: absolute; left: 31px; top: 20px; }
  .footer a { color: var(--white); }
  .to-top { position: absolute; left: 676px; top: 22px; }
</style>
</head>
<body>
  <header class="hero">
    <div class="hero-photo" role="img" aria-label="Photo of a man with diabetes in a pink shirt, softly out of focus"></div>
    <div class="brand">sucrana</div>
    <nav class="nav"><a href="#">Promo</a><a href="#">Offer</a><a href="#">Contact</a></nav>
    <h1 class="hero-title">GET UP TO <u>75% OFF</u><br>ALL YOUR DIABETIC SUPPLIES GUARANTEED</h1>
    <div class="hero-rule"></div>
    <p class="hero-sub">Never Pay Full Price For Your Diabetic Supplies Again!</p>
  </header>

  <form class="brand-form">
    <p class="form-intro">Choose Your Current Brand Of Diabetic Supplies<br>That You Currently Use To See If They Are<br>Covered Under Our Free Diabetic RX Assistance Program:</p>
    <div class="brand-select">
      <div class="select-head">SELECT BRAND
        <span class="select-caret"><svg width="24" height="24" viewBox="0 0 24 24"><path d="M9.5 10.5h5l-2.5 3z" fill="#fff"/></svg></span>
      </div>
      <div class="option">ACARBOSE - <b>75% OFF</b><span class="radio"></span></div>
      <div class="option is-selected">ZERNOVAB TEL - <b>75% OFF</b><span class="radio"></span></div>
      <div class="option">ZERNOVAB TEL X - <b>75% OFF</b><span class="radio"></span></div>
      <span class="scrollbar"></span>
    </div>
    <div class="choose-btn">CHOOSE BRAND</div>
  </form>

  <section>
    <h2 class="healthy-title">FRESH AND HEALTHY<br>KEEP AWAY YOU FROM<br>DIABETES</h2>
    <div class="healthy-image" role="img" aria-label="Bowl of fruit with pineapple, apples and strawberries beside a hand holding a glucose meter"></div>
  </section>

  <section class="tips" role="img" aria-label="Photo of a doctor talking with a patient">
    <h2 class="tips-title">TIPS TO AVOID DIABETES</h2>
    <div class="tips-btn">LET ME KNOW</div>
  </section>

  <footer class="footer">
    <p>Copyright © 2017, All rights reserved. <a href="#">Privacy &amp; Policy</a></p>
    <svg class="to-top" width="14" height="10" viewBox="0 0 14 10"><path d="M2 8l5-5 5 5" stroke="#1a5d66" stroke-width="2.5" fill="none"/></svg>
  </footer>
</body>
</html>
```